**** Web design project for VornaSoft ****

For my ICT company VornaSoft I need a website.

We design, build and host web-applications and we have our own CMS product. In the references part we want to show sample websites (thumbnails) + links.

It should look modern (WEB 2.0), rounded corners.

I want the following menu' s:
- Home
- Services
- References
- News
- About VornaSoft
- Contact

Sample websites:
See attachments
http://www.plumvest.com
http://www.gadomirbureauwerk.nl

Reason: Want to take some time for feedback and improvements.

Reason: I'm waiting for a black background, with shadow and ambient light. You'll make a good chance!

Industry/Entity Type

It Company

Requirements
Must have
• - Fixed width (1024px), should fit on an IPad2
- Language selection English/Dutch
- Twitter/Facebook/LinkedIn/RSS icons
- Footer for Terms of use and Copyrights
- Search box
- 3 (or more) boxes for information i.e. news, blog or advertisements
Nice to have
• - Footer Site Map
- Contrasting background outside borders
- wide image (rotator) (with transperant sentence block)
- Shadow

```html
<!DOCTYPE html>
<html lang="en">
<head>
<meta charset="utf-8">
<title>VornaSoft</title>
<link href="https://fonts.googleapis.com/css2?family=Arimo:wght@400;700&display=swap" rel="stylesheet">
<style>
:root{
  --blue:#1e94dc;
  --sky:#63b5ea;
  --slate:#5f7f8c;
  --grey-text:#4a4a4a;
  --heading-grey:#9a9a9a;
  --link:#1a8fd6;
  --white:#fff;
}
*{box-sizing:border-box;margin:0;padding:0}
html,body{width:1182px;height:1200px;overflow:hidden;background:#fff}
body{font-family:"Arimo",Arial,sans-serif;color:var(--grey-text);position:relative}
.topline{position:absolute;left:0;top:0;width:1182px;height:9px;background:var(--blue)}
.header{position:absolute;left:0;top:9px;width:1182px;height:107px;background:linear-gradient(#f6f1f3,#fff)}
.brand{position:absolute;left:138px;top:12px;display:flex;align-items:center;gap:12px}
.brand-dot{width:76px;height:76px;border-radius:50%;background:var(--blue)}
.brand-name{font-size:32px;color:var(--slate);font-weight:400;letter-spacing:1px}
.search{position:absolute;left:774px;top:50px;width:270px;height:37px;border:2px solid #ddd;border-radius:8px;background:#fff;display:flex;overflow:hidden}
.search-field{flex:1;display:flex;align-items:center;padding-left:12px;gap:8px;font-size:11px;color:#aaa}
.search-btn{width:68px;background:linear-gradient(#3aa6e8,#1a7fcc);color:#fff;font-size:12px;display:flex;align-items:center;justify-content:center}
.band{position:absolute;left:0;top:116px;width:1182px;height:397px;background:linear-gradient(#6cc0ef 0%,#62b3e8 80%,#3e8ed2 100%)}
.nav{position:absolute;left:138px;top:117px;width:905px;height:42px;border-radius:0 0 8px 8px;background:linear-gradient(#3c8fe0,#1f5fc6);display:flex;align-items:center;box-shadow:0 2px 4px rgba(0,0,0,.2)}
.nav a{color:#fff;text-decoration:none;font-size:12.5px;height:42px;display:flex;align-items:center;justify-content:center;border-right:1px solid rgba(255,255,255,.3)}
.nav a.active{background:linear-gradient(#465a8c,#2c3c6e);border-radius:0 0 0 8px}
.lang{position:absolute;right:12px;top:9px;width:156px;height:22px;background:#fff;border-radius:3px;font-size:11px;color:#333;display:flex;align-items:center;justify-content:space-between;padding:0 10px}
.banner{position:absolute;left:138px;top:186px;width:905px;height:294px;border-radius:8px;border:1px solid #fff;overflow:hidden;background:radial-gradient(circle at 30% 45%,#4a8fa8,#1c3040 55%,#0e1620);box-shadow:3px 4px 6px rgba(0,0,0,.35)}
.banner-caption{position:absolute;left:0;bottom:0;width:100%;height:50px;background:rgba(10,12,20,.6);color:#6fd0f2;font-size:22px;font-style:italic;text-align:right;padding:12px 14px 0 0}
.dots{position:absolute;left:566px;top:494px;display:flex;gap:6px}
.dots span{width:10px;height:10px;border-radius:50%;background:#fff}
.dots span.on{background:#243a70}
.welcome-title{position:absolute;left:140px;top:530px;font-size:26px;font-weight:400;color:var(--heading-grey)}
.welcome-title b{font-weight:400;color:var(--slate)}
.welcome-photo{position:absolute;left:139px;top:575px;width:195px;height:165px;border-radius:6px;background:linear-gradient(135deg,#8a8a8a,#b8b1a6 50%,#555);box-shadow:3px 4px 5px rgba(0,0,0,.35)}
.welcome-text{position:absolute;left:350px;top:572px;width:682px;font-size:10.4px;line-height:17.5px;color:#555}
.welcome-text p+p{margin-top:17.5px}
.btn-more{position:absolute;left:933px;top:718px;width:84px;height:30px;border-radius:5px;background:linear-gradient(#8aa4ae,#5c7883);border:3px solid #eef2f3;color:#fff;font-size:11px;font-weight:700;display:flex;align-items:center;justify-content:center;box-shadow:0 1px 3px rgba(0,0,0,.3)}
.featured-title{position:absolute;left:140px;top:774px;font-size:25px;font-weight:400;color:var(--blue)}
.arrow{position:absolute;top:914px;width:37px;height:35px;border-radius:50%;display:flex;align-items:center;justify-content:center}
.arrow.prev{left:142px;background:#d9d9d9}
.arrow.next{left:1003px;background:#6e8893}
.box{position:absolute;top:814px;width:246px;height:227px;border-radius:8px;background:#fff;border:1px solid #ccc;box-shadow:4px 5px 5px rgba(0,0,0,.3);overflow:hidden}
.box-head{height:41px;background:linear-gradient(#8ea6ae,#5a7782);color:#fff;font-size:20px;padding:9px 12px;border-bottom:3px solid #dfe5e7}
.item{display:flex;gap:8px;padding:10px 12px 0 12px;height:71px}
.item-title{color:var(--link);font-size:11px;font-weight:700}
.item-desc{font-size:11.5px;line-height:18px;color:#555;margin-top:3px}
.cal{width:50px;height:56px;border-radius:3px;border:1px solid #999;background:#fff;flex:none;overflow:hidden}
.cal-month{height:16px;background:var(--blue);color:#fff;font-size:10px;padding-left:4px}
.cal-day{font-size:24px;font-weight:700;color:#222;text-align:center;line-height:34px}
.thumb{width:54px;height:48px;border:1px solid #ccc;background:#dcdcdc;flex:none;margin-top:4px}
.thumb.ad{background:linear-gradient(135deg,#3d6fb5,#8fb0d8)}
.meta{font-size:9.5px;line-height:13px;color:#444;display:flex;align-items:center;gap:4px}
.meta i{width:9px;height:9px;border-radius:50%;background:#3d82c8;display:inline-block}
.meta a{color:var(--link);text-decoration:none}
.box-link{position:absolute;right:34px;bottom:22px;color:var(--link);font-size:11px;font-weight:700;text-decoration:underline}
.foot-line{position:absolute;left:0;top:1068px;width:1182px;height:8px;background:var(--blue)}
.footer{position:absolute;left:0;top:1077px;width:1182px;height:123px;background:linear-gradient(#7e9aa3,#4f6d7a)}
.foot-brand{position:absolute;left:140px;top:38px;display:flex;align-items:center;gap:8px}
.foot-brand .brand-dot{width:46px;height:46px;background:#fff}
.foot-brand .brand-name{font-size:24px;color:#fff}
.follow{position:absolute;left:750px;top:24px;display:flex;align-items:center;gap:11px;color:#fff;font-size:15px}
.social{width:28px;height:28px;border-radius:4px}
.copy{position:absolute;left:750px;top:77px;font-size:10px;color:#fff}
</style>
</head>
<body>
<div class="topline"></div>
<header class="header">
  <div class="brand"><span class="brand-dot"></span><span class="brand-name">VornaSoft</span></div>
  <div class="search">
    <div class="search-field">
      <svg width="16" height="16" viewBox="0 0 16 16"><circle cx="9.5" cy="6.5" r="5" fill="none" stroke="#777" stroke-width="1.5"/><line x1="6" y1="10" x2="1.5" y2="14.5" stroke="#777" stroke-width="2"/></svg>
      Enter search here
    </div>
    <div class="search-btn">Search</div>
  </div>
</header>
<div class="band"></div>
<nav class="nav">
  <a class="active" style="width:80px">Home</a><a style="width:99px">Services</a><a style="width:116px">References</a><a style="width:79px">News</a><a style="width:80px">About</a><a style="width:102px">VornaSoft</a><a style="width:90px">Contact</a>
  <div class="lang">Select Language <svg width="9" height="6"><path d="M0 0h9L4.5 6z" fill="#444"/></svg></div>
</nav>
<div class="banner" role="img" aria-label="Rotating banner image: robot touching a glowing digital globe and screens">
  <div class="banner-caption">Banner Content to be placed here...</div>
</div>
<div class="dots"><span class="on"></span><span></span><span></span><span></span></div>

<h1 class="welcome-title">Welcome to <b>VornaSoft</b></h1>
<div class="welcome-photo" role="img" aria-label="Photo of business people working at a laptop"></div>
<div class="welcome-text">
  <p>Lorem Ipsum is simply dummy text of the printing and typesetting industry. Lorem Ipsum has been the industry's standard dummy text ever since the 1500s, when an unknown printer took a galley of type and scrambled it to make a type specimen book. It has survived not only five centuries, but also the leap into electronic typesetting, remaining essentially unchanged. It was popularised in the 1960s with the release of Inkset sheets containing Lorem Ipsum passages, and more recently with desktop publishing software like Folio Layout including versions of Lorem Ipsum.</p>
  <p>Lorem Ipsum is simply dummy text of the printing and typesetting industry. Lorem Ipsum has been the industry's standard dummy text ever since the 1500s, when an unknown printer took a galley of type and scrambled it to make a type specimen book.</p>
</div>
<div class="btn-more">Read More</div>

<h2 class="featured-title">Featured Services</h2>
<div class="arrow prev"><svg width="14" height="14"><path d="M10 2L4 7l6 5" fill="none" stroke="#fff" stroke-width="3"/></svg></div>
<div class="arrow next"><svg width="14" height="14"><path d="M4 2l6 5-6 5" fill="none" stroke="#fff" stroke-width="3"/></svg></div>

<section class="box" style="left:192px">
  <div class="box-head">News</div>
  <div class="item"><div class="cal"><div class="cal-month">SEP</div><div class="cal-day">12</div></div><div><div class="item-title">News Heading 1</div><div class="item-desc">Lorem ipsum dolor sit amet consecutor...</div></div></div>
  <div class="item"><div class="cal"><div class="cal-month">SEP</div><div class="cal-day">12</div></div><div><div class="item-title">News Heading 1</div><div class="item-desc">Lorem ipsum dolor sit amet consecutor...</div></div></div>
  <a class="box-link">More News &gt;&gt;</a>
</section>

<section class="box" style="left:464px">
  <div class="box-head">Blog</div>
  <div class="item"><div class="thumb" role="img" aria-label="Author avatar placeholder"></div><div><div class="item-title">Blog 1</div><div class="meta"><i></i>1 day 15 hours ago</div><div class="meta"><i></i>1 Comment</div><div class="meta"><i style="background:#888"></i><a>http://www.quillpost.com</a></div></div></div>
  <div class="item"><div class="thumb" role="img" aria-label="Author avatar placeholder"></div><div><div class="item-title">Blog 1</div><div class="meta"><i></i>1 day 15 hours ago</div><div class="meta"><i></i>1 Comment</div><div class="meta"><i style="background:#888"></i><a>http://www.quillpost.com</a></div></div></div>
  <a class="box-link">View All &gt;&gt;</a>
</section>

<section class="box" style="left:738px">
  <div class="box-head">Advertisements</div>
  <div class="item"><div class="thumb ad" role="img" aria-label="Advertisement sign illustration"></div><div><div class="item-title">Advertisement 1</div><div class="item-desc">Lorem ipsum dolor sit amet consecutor...</div></div></div>
  <div class="item"><div class="thumb ad" role="img" aria-label="Advertisement sign illustration"></div><div><div class="item-title">Advertisement 2</div><div class="item-desc">Lorem ipsum dolor sit amet consecutor...</div></div></div>
  <a class="box-link">Create New Ad &gt;&gt;</a>
</section>

<div class="foot-line"></div>
<footer class="footer">
  <div class="foot-brand"><span class="brand-dot"></span><span class="brand-name">VornaSoft</span></div>
  <div class="follow">Follow us on :
    <span class="social" style="background:#2a7fc0" aria-label="Professional network profile"></span>
    <span class="social" style="background:#f08a1c" aria-label="News feed"></span>
    <span class="social" style="background:#5cc8ec" aria-label="Microblog profile"></span>
    <span class="social" style="background:#3b5b9a" aria-label="Social network page"></span>
  </div>
  <div class="copy">Copyright © 2012 VornaSoft. All Rights Reserved &nbsp;&nbsp;&nbsp; | &nbsp;&nbsp;&nbsp; Terms of Use</div>
</footer>
</body>
</html>
```